Illustrate Our Process "Bright Path Method"

We need a graphic design to brand our proprietary process. We are a wealth services team that serves a group of individual and families. Most financial advisors only provide investment management. Our team implements a process that puts our clients goals and finances on a Bright Path foundation.

Please create your own graphic that will simply explain that our elevated process will take care of a client's complete financial picture and in turn put them on a Bright Path foundation.

Our process is called the "Bright Path Method" and it involves:
1) Wealth Management
2) Tax Strategy
3) Cash Management
4) Risk Management
5) Estate Strategy
6) Philanthropy
7) Value Added Services
Note: These things were uploaded in "Bright Path A"

As a person's life becomes more complex they will grow into our process which will constantly ensure their finances & goals are on a Bright Path foundation.

I uploaded pictures of our office so you can see what might go with the overall look and feel of our office if that helps.

Industry/Entity Type

Finance

Requirements
Must have
• The final design should communicate simplicity, stability, expertise and trust. We also want a final design that will quickly describe our process instead of creating confusion.
Nice to have
• We are wanting to put the final design on a canvas print on our bookshelf (which is attached) and have the ability to blow it up and put it on one of our walls.
Should not have
• Clash with the feel and decor of our office

```html
<!DOCTYPE html>
<html lang="en">
<head>
<meta charset="utf-8">
<title>Bright Path Method</title>
<link rel="stylesheet" href="https://fonts.googleapis.com/css2?family=Oswald:wght@500;700&display=swap">
<style>
  :root {
    --page: #f2f1ef;
    --amber-light: #f8c958;
    --amber: #f0a236;
    --orange: #e07428;
    --rust: #c24a22;
    --rust-deep: #a8351c;
    --brown: #5a2313;
    --brown-arc: #6e2a14;
    --ring-orange: #e46a24;
    --ring-red: #c93f1d;
    --ring-blue: #3b78c4;
    --ring-blue-light: #86b8e6;
    --white: #ffffff;
    --frame: #1e1e1e;
  }
  html, body {
    margin: 0;
    padding: 0;
    width: 1200px;
    height: 844px;
    overflow: hidden;
    background: var(--page);
  }
  .poster {
    position: absolute;
    left: 0;
    top: 117px;
    width: 1200px;
    height: 610px;
    display: block;
  }
  .title {
    font-family: "Oswald", sans-serif;
    font-weight: 700;
    font-size: 62px;
    fill: var(--brown);
    letter-spacing: -1px;
  }
  .step-label {
    font-family: "Oswald", sans-serif;
    font-weight: 500;
    font-size: 17px;
    fill: var(--brown);
    letter-spacing: -0.4px;
  }
  .stop-amber-light { stop-color: var(--amber-light); }
  .stop-amber { stop-color: var(--amber); }
  .stop-orange { stop-color: var(--orange); }
  .stop-rust { stop-color: var(--rust); }
  .stop-rust-deep { stop-color: var(--rust-deep); }
  .stop-ring-orange { stop-color: var(--ring-orange); }
  .stop-ring-red { stop-color: var(--ring-red); }
  .stop-ring-blue { stop-color: var(--ring-blue); }
  .stop-ring-blue-light { stop-color: var(--ring-blue-light); }
  .stop-clear { stop-color: var(--amber-light); stop-opacity: 0; }
  .connector { stroke: var(--white); stroke-width: 1.4; opacity: .9; }
  .connector-dark { stroke: var(--brown-arc); stroke-width: 1.6; }
  .halo { fill: none; stroke: var(--white); stroke-width: 1; opacity: .75; }
  .arc-light { fill: none; stroke: var(--white); stroke-width: 7; stroke-linecap: round; }
  .arc-dark { fill: none; stroke: var(--brown-arc); stroke-width: 7; stroke-linecap: round; }
  .ring-warm { fill: url(#ringWarm); }
  .ring-cool { fill: url(#ringCool); }
  .face { fill: var(--white); }
  .spark { fill: var(--white); }
</style>
</head>
<body>
<svg class="poster" viewBox="0 0 1200 610" xmlns="http://www.w3.org/2000/svg" aria-labelledby="posterTitle">
  <title id="posterTitle">Bright Path Method: seven-step wealth services process</title>
  <defs>
    <linearGradient id="bgBase" x1="0" y1="0" x2="1" y2="1">
      <stop offset="0" class="stop-rust"/>
      <stop offset=".35" class="stop-amber"/>
      <stop offset=".6" class="stop-amber-light"/>
      <stop offset=".85" class="stop-orange"/>
      <stop offset="1" class="stop-rust"/>
    </linearGradient>
    <radialGradient id="glowGold" cx=".55" cy=".25" r=".45">
      <stop offset="0" class="stop-amber-light"/>
      <stop offset="1" class="stop-clear"/>
    </radialGradient>
    <radialGradient id="shadeRust" cx=".15" cy=".1" r=".45">
      <stop offset="0" class="stop-rust-deep"/>
      <stop offset="1" class="stop-clear"/>
    </radialGradient>
    <radialGradient id="shadeRight" cx=".85" cy=".75" r=".35">
      <stop offset="0" class="stop-rust-deep"/>
      <stop offset="1" class="stop-clear"/>
    </radialGradient>
    <linearGradient id="barFill" x1="0" y1="0" x2="1" y2="0">
      <stop offset="0" class="stop-rust-deep"/>
      <stop offset="1" class="stop-orange"/>
    </linearGradient>
    <linearGradient id="ringWarm" x1="0" y1="0" x2="1" y2="1">
      <stop offset="0" class="stop-ring-orange"/>
      <stop offset="1" class="stop-ring-red"/>
    </linearGradient>
    <linearGradient id="ringCool" x1="0" y1="1" x2="1" y2="0">
      <stop offset="0" class="stop-ring-blue"/>
      <stop offset="1" class="stop-ring-blue-light"/>
    </linearGradient>
  </defs>

  <!-- Background -->
  <rect width="1200" height="610" fill="url(#bgBase)"/>
  <rect width="1200" height="610" fill="url(#shadeRust)"/>
  <rect width="1200" height="610" fill="url(#shadeRight)"/>
  <rect width="1200" height="610" fill="url(#glowGold)"/>
  <rect class="world-map" x="180" y="40" width="880" height="520" fill="var(--amber-light)" opacity=".12" role="img" aria-label="Faint dotted world map behind the process steps"/>
  <rect x="0" y="0" width="1200" height="610" fill="none" stroke="var(--frame)" stroke-width="5"/>

  <!-- Sparkles -->
  <g class="sparkles">
    <circle class="spark" cx="86" cy="30" r="1.8"/>
    <circle class="spark" cx="86" cy="75" r="2.4"/>
    <circle class="spark" cx="7" cy="126" r="1.8"/>
    <circle class="spark" cx="60" cy="265" r="1.6"/>
    <circle class="spark" cx="104" cy="573" r="2.2"/>
    <circle class="spark" cx="1137" cy="165" r="1.8"/>
    <circle class="spark" cx="1130" cy="500" r="1.8"/>
    <circle class="spark" cx="1138" cy="549" r="1.6"/>
    <path class="spark" d="M269 25 l2 4 4 2 -4 2 -2 4 -2 -4 -4 -2 4 -2z"/>
    <path class="spark" d="M992 107 l2.4 5 5 2.4 -5 2.4 -2.4 5 -2.4 -5 -5 -2.4 5 -2.4z"/>
    <path class="spark" d="M40 434 l2 4 4 2 -4 2 -2 4 -2 -4 -4 -2 4 -2z"/>
    <path class="spark" d="M203 526 l2 4 4 2 -4 2 -2 4 -2 -4 -4 -2 4 -2z"/>
    <path class="spark" d="M909 563 l2 4 4 2 -4 2 -2 4 -2 -4 -4 -2 4 -2z"/>
  </g>

  <!-- Title and header bar -->
  <text class="title" x="595" y="140" text-anchor="middle">BRIGHT PATH METHOD</text>
  <rect x="61" y="159" width="1012" height="13" rx="6.5" fill="url(#barFill)"/>
  <circle cx="65" cy="165.5" r="3" fill="var(--orange)"/>
  <circle cx="1080" cy="165.5" r="3" fill="var(--white)"/>
  <line x1="68" y1="177" x2="1066" y2="177" stroke="var(--white)" stroke-width="1.4"/>

  <!-- Lower row: warm steps -->
  <g class="step step-warm">
    <line class="connector" x1="153" y1="177" x2="153" y2="361"/>
    <circle class="halo" cx="153" cy="444" r="82"/>
    <path class="arc-light" d="M72 435 A82 82 0 0 1 234 435"/>
    <circle class="ring-warm" cx="153" cy="444" r="68"/>
    <circle class="face" cx="153" cy="444" r="51"/>
    <text class="step-label" x="153" y="441" text-anchor="middle">TAX</text>
    <text class="step-label" x="153" y="462" text-anchor="middle">STRATEGY</text>
  </g>
  <g class="step step-warm">
    <line class="connector" x1="474" y1="177" x2="474" y2="361"/>
    <circle class="halo" cx="474" cy="444" r="82"/>
    <path class="arc-light" d="M398 478 A82 82 0 0 1 536 391"/>
    <circle class="ring-warm" cx="474" cy="444" r="68"/>
    <circle class="face" cx="474" cy="444" r="51"/>
    <text class="step-label" x="474" y="441" text-anchor="middle">ESTATE</text>
    <text class="step-label" x="474" y="462" text-anchor="middle">STRATEGY</text>
  </g>
  <g class="step step-warm">
    <line class="connector" x1="762" y1="177" x2="762" y2="361"/>
    <circle class="halo" cx="762" cy="444" r="82"/>
    <path class="arc-light" d="M705 386 A82 82 0 0 1 840 472"/>
    <circle class="ring-warm" cx="762" cy="444" r="68"/>
    <circle class="face" cx="762" cy="444" r="51"/>
    <text class="step-label" x="762" y="441" text-anchor="middle">VALUE ADDED</text>
    <text class="step-label" x="762" y="462" text-anchor="middle">SERVICES</text>
  </g>
  <g class="step step-warm">
    <line class="connector" x1="1055" y1="177" x2="1055" y2="361"/>
    <circle class="halo" cx="1055" cy="444" r="82"/>
    <path class="arc-light" d="M975 430 A82 82 0 0 1 1135 430"/>
    <circle class="ring-warm" cx="1055" cy="444" r="68"/>
    <circle class="face" cx="1055" cy="444" r="51"/>
    <text class="step-label" x="1055" y="451" text-anchor="middle">PHILANTHROPY</text>
  </g>

  <!-- Upper row: cool steps -->
  <g class="step step-cool">
    <line class="connector-dark" x1="328" y1="177" x2="328" y2="224"/>
    <circle class="halo" cx="328" cy="307" r="82"/>
    <path class="arc-dark" d="M348 226 A82 82 0 0 0 290 380"/>
    <circle class="ring-cool" cx="328" cy="307" r="68"/>
    <circle class="face" cx="328" cy="307" r="51"/>
    <text class="step-label" x="328" y="304" text-anchor="middle">WEALTH</text>
    <text class="step-label" x="328" y="325" text-anchor="middle">MANAGEMENT</text>
  </g>
  <g class="step step-cool">
    <line class="connector-dark" x1="618" y1="177" x2="618" y2="224"/>
    <circle class="halo" cx="618" cy="307" r="82"/>
    <path class="arc-dark" d="M537 324 A82 82 0 0 1 692 272"/>
    <circle class="ring-cool" cx="618" cy="307" r="68"/>
    <circle class="face" cx="618" cy="307" r="51"/>
    <text class="step-label" x="618" y="304" text-anchor="middle">CASH</text>
    <text class="step-label" x="618" y="325" text-anchor="middle">MANAGEMENT</text>
  </g>
  <g class="step step-cool">
    <line class="connector-dark" x1="906" y1="177" x2="906" y2="224"/>
    <circle class="halo" cx="906" cy="307" r="82"/>
    <path class="arc-dark" d="M876 231 A82 82 0 0 1 963 366"/>
    <circle class="ring-cool" cx="906" cy="307" r="68"/>
    <circle class="face" cx="906" cy="307" r="51"/>
    <text class="step-label" x="906" y="304" text-anchor="middle">RISK</text>
    <text class="step-label" x="906" y="325" text-anchor="middle">MANAGEMENT</text>
  </g>
</svg>
</body>
</html>
```